Seller Looking for a luxurious diverse ethnic look...stunning but not overly seductive

I need a web Design for a company based in NEW YORK CITY called Velvet Harbor LLC. Initially I will be selling clothing and accessories as well as electronics on Tradora and hope to branch out. I want the whole experience for my customers and people I will buy from when they deal with me to be confident that this will be a velvet harbor and luxurious transaction.
Updates

Project Deadline Extended Reason: As I keep getting these great designs I continue to get more ideas and feel more time will help get us there. Added Thursday, July 16, 2015

Target Market(s)

ages 20-60

Industry/Entity Type

Clothing

Number of Pages Required

1 page

Font styles to use
Script

Colors
b768aa

Requirements
Must have
• Sleek and Luxurious feel and modern. I would like the page to look startling stunning yet not overly seductive and to include ethnic diversity. I like the illusion not knowing what the sight is selling since I am not targeting one area.
Should not have
• Do not want it to look generic or traditional

```html
<!DOCTYPE html>
<html lang="en">
<head>
<meta charset="utf-8">
<title>Velvet Harbor LLC — Store</title>
<link href="https://fonts.googleapis.com/css2?family=Open+Sans:wght@400;600;700&display=swap" rel="stylesheet">
<style>
:root{
  --brand:#b768aa;
  --brand-dark:#8e4b84;
  --ink:#3a3a44;
  --muted:#8a8a94;
  --line:#dedee4;
  --topbar:#f1f1f4;
  --footer:#ebebef;
  --footer-bottom:#dcdce2;
  --white:#ffffff;
}
*{box-sizing:border-box;margin:0;padding:0}
html,body{width:849px;height:1200px;overflow:hidden}
body{font-family:"Open Sans",Arial,sans-serif;color:var(--ink);background:var(--white);position:relative}
a{color:inherit;text-decoration:none}

.topbar{height:28px;background:var(--topbar);border-bottom:1px solid var(--line);display:flex;align-items:center;justify-content:space-between;padding:0 36px;font-size:10px;color:var(--muted)}
.topbar-links{display:flex;gap:16px}
.topbar-tools{display:flex;align-items:center;gap:14px}
.search{width:110px;height:16px;border:1px solid var(--line);background:var(--white);font-size:9px;padding:0 6px;display:flex;align-items:center;gap:4px;color:var(--muted)}
.cart{display:flex;align-items:center;gap:4px}

.header{height:85px;display:flex;align-items:center;justify-content:space-between;padding:0 36px 0 28px}
.brand{display:flex;align-items:center;gap:10px}
.brand-mark{width:22px;height:22px;background:var(--brand)}
.brand-name{font-size:22px;font-weight:600;color:var(--brand)}
.nav{display:flex;gap:22px;font-size:11px;color:var(--muted);margin-top:14px}
.nav .active{color:var(--brand)}

.hero{position:relative;height:334px;
  background:
    radial-gradient(ellipse 260px 200px at 690px 150px,rgba(246,232,210,.95),rgba(246,232,210,0) 70%),
    radial-gradient(ellipse 90px 40px at 650px 205px,rgba(196,92,128,.55),rgba(196,92,128,0) 80%),
    radial-gradient(ellipse 180px 160px at 470px 250px,rgba(214,120,150,.55),rgba(214,120,150,0) 75%),
    radial-gradient(ellipse 160px 140px at 520px 120px,rgba(176,122,92,.75),rgba(176,122,92,0) 75%),
    linear-gradient(100deg,#5a4443 0%,#7d5a52 22%,#b48a74 42%,#d9b9a3 58%,#efe1cc 78%,#d8c3aa 100%)}
.hero-copy{position:absolute;left:22px;top:64px;color:var(--white)}
.hero-title{font-size:25px;font-weight:700;letter-spacing:.2px}
.hero-rule{width:110px;height:2px;background:var(--white);margin:12px 0 14px}
.hero-tagline{font-size:19px;font-weight:700;line-height:1.3;width:290px}

.products{padding:26px 76px 0}
.section-title{font-size:15px;font-weight:600;color:var(--ink);padding-bottom:8px;border-bottom:1px solid var(--line)}
.product-grid{display:grid;grid-template-columns:repeat(4,155px);column-gap:24px;row-gap:30px;margin-top:14px}
.product{text-align:center}
.product-media{width:155px;height:155px;border:1px solid var(--line);background:var(--white)}
.media-phones{background:radial-gradient(circle at 50% 50%,#2a2d33 0,#5b6068 28%,#c9ccd2 48%,#fff 68%)}
.media-watches{background:radial-gradient(ellipse 55% 40% at 50% 50%,#c9a25a 0,#8a7a5a 30%,#e8dcc0 55%,#fff 75%)}
.media-sunglasses{background:radial-gradient(ellipse 50% 22% at 50% 50%,#1e1e22 0,#55565c 40%,#e4e4e8 70%,#fff 85%)}
.media-shoes{background:radial-gradient(ellipse 45% 38% at 50% 55%,#2b2224 0,#7a6a64 35%,#e2dad6 62%,#fff 80%)}
.media-hats{background:radial-gradient(ellipse 55% 30% at 50% 52%,#cdbca0 0,#e3d6bf 40%,#f4eee4 65%,#fff 82%)}
.media-jacket{background:radial-gradient(ellipse 40% 45% at 50% 50%,#111214 0,#2c2d31 45%,#b6b7bc 70%,#fff 88%)}
.media-headphones{background:radial-gradient(ellipse 42% 45% at 50% 50%,#d8d8dc 0,#2a2a2e 30%,#c0343a 42%,#e9e9ec 62%,#fff 80%)}
.media-bags{background:radial-gradient(ellipse 38% 45% at 50% 55%,#6f7782 0,#9aa1aa 40%,#d9dce0 65%,#fff 82%)}
.product-name{font-size:10px;font-weight:600;margin-top:6px}
.product-price{font-size:9px;color:var(--brand)}
.arrow{position:absolute;top:682px;width:14px;height:24px}
.arrow.left{left:12px}.arrow.right{right:12px}

.footer{position:absolute;left:0;top:946px;width:849px;height:214px;background:var(--footer);padding:26px 34px 0}
.footer-cols{display:grid;grid-template-columns:234px 200px 190px 190px}
.footer-brand .brand-name{font-size:18px}
.contact{list-style:none;margin-top:14px;font-size:9px;color:var(--muted)}
.contact li{display:flex;align-items:center;gap:8px;height:24px}
.contact-icon{width:16px;height:16px;background:var(--white);border:1px solid var(--line);display:flex;align-items:center;justify-content:center}
.col-title{font-size:10px;font-weight:600;color:var(--muted);margin-top:6px;margin-bottom:10px}
.mini{list-style:none}
.mini li{display:flex;align-items:center;justify-content:space-between;height:28px;padding-right:40px;font-size:9px}
.mini-name{font-weight:600;color:var(--ink)}
.mini-price{display:block;color:var(--brand);font-weight:400}
.mini-thumb{width:24px;height:16px;border-radius:3px}
.t-phones{background:linear-gradient(135deg,#2a2d33,#8c9099)}
.t-watches{background:linear-gradient(135deg,#c9a25a,#6e6350)}
.t-sunglasses{background:linear-gradient(135deg,#1e1e22,#7a7b82)}
.t-hats{background:linear-gradient(135deg,#e3d6bf,#b9a686)}
.t-shoes{background:linear-gradient(135deg,#2b2224,#8a7a74)}
.t-jacket{background:linear-gradient(135deg,#111214,#4a4b50)}
.t-headphones{background:linear-gradient(135deg,#2a2a2e,#c0343a)}
.t-bags{background:linear-gradient(135deg,#6f7782,#b8bec6)}
.footer-bottom{position:absolute;left:0;top:1160px;width:849px;height:40px;background:var(--footer-bottom);display:flex;align-items:center;justify-content:center;gap:10px;font-size:9px;color:var(--muted)}
.footer-bottom strong{color:var(--ink)}
</style>
</head>
<body>
<div class="topbar">
  <nav class="topbar-links"><a href="#">My Products</a><a href="#">Templates</a></nav>
  <div class="topbar-tools">
    <a href="#">Log In</a>
    <div class="search"><svg width="8" height="8" viewBox="0 0 10 10"><circle cx="4" cy="4" r="3" fill="none" stroke="#8a8a94" stroke-width="1.3"/><line x1="6.3" y1="6.3" x2="9.3" y2="9.3" stroke="#8a8a94" stroke-width="1.3"/></svg>Search Products</div>
    <span class="cart"><svg width="11" height="10" viewBox="0 0 12 10"><path d="M0 1h2l1.5 6h6.5l1.5-4.5H3" fill="none" stroke="#8a8a94" stroke-width="1.2"/><circle cx="4.5" cy="9" r=".9" fill="#8a8a94"/><circle cx="9" cy="9" r=".9" fill="#8a8a94"/></svg>$0.00</span>
  </div>
</div>

<header class="header">
  <div class="brand"><span class="brand-mark"></span><span class="brand-name">Velvet Harbor LLC</span></div>
  <nav class="nav"><a class="active" href="#">Home</a><a href="#">Shop</a><a href="#">Blog</a><a href="#">Sample</a><a href="#">Page</a><a href="#">Templates</a></nav>
</header>

<section class="hero" role="img" aria-label="Woman of color in a pink plaid shirt, seen from behind, holding a cream straw sun hat with a pink band">
  <div class="hero-copy">
    <h1 class="hero-title">Welcome to our store</h1>
    <div class="hero-rule"></div>
    <p class="hero-tagline">We hand make the most awesomest products in the world</p>
  </div>
</section>

<section class="products">
  <h2 class="section-title">Recent Products</h2>
  <div class="product-grid">
    <div class="product"><div class="product-media media-phones" role="img" aria-label="Two smartphones"></div><p class="product-name">New Phones</p><p class="product-price">$99 $119</p></div>
    <div class="product"><div class="product-media media-watches" role="img" aria-label="Pair of gold wristwatches"></div><p class="product-name">Watches Class</p><p class="product-price">$210</p></div>
    <div class="product"><div class="product-media media-sunglasses" role="img" aria-label="Dark sunglasses"></div><p class="product-name">Sunglasses</p><p class="product-price">$75 $60</p></div>
    <div class="product"><div class="product-media media-shoes" role="img" aria-label="High-heeled shoe"></div><p class="product-name">Shoes</p><p class="product-price">$120</p></div>
    <div class="product"><div class="product-media media-hats" role="img" aria-label="Cream fedora hat"></div><p class="product-name">Fashion Hats</p><p class="product-price">$38 $45</p></div>
    <div class="product"><div class="product-media media-jacket" role="img" aria-label="Black leather jacket"></div><p class="product-name">Jacket</p><p class="product-price">$175</p></div>
    <div class="product"><div class="product-media media-headphones" role="img" aria-label="Over-ear headphones"></div><p class="product-name">Headphones</p><p class="product-price">$55 $68</p></div>
    <div class="product"><div class="product-media media-bags" role="img" aria-label="Grey tote bag"></div><p class="product-name">Bags-accessories</p><p class="product-price">$89</p></div>
  </div>
</section>
<svg class="arrow left" viewBox="0 0 14 24"><polyline points="12,2 2,12 12,22" fill="none" stroke="#c4c4cc" stroke-width="2"/></svg>
<svg class="arrow right" viewBox="0 0 14 24"><polyline points="2,2 12,12 2,22" fill="none" stroke="#c4c4cc" stroke-width="2"/></svg>

<footer class="footer">
  <div class="footer-cols">
    <div class="footer-brand">
      <div class="brand"><span class="brand-mark"></span><span class="brand-name">Velvet Harbor LLC</span></div>
      <ul class="contact">
        <li><span class="contact-icon"><svg width="10" height="10" viewBox="0 0 10 10"><path d="M1 5L5 1.5 9 5M2.5 4v5h5V4" fill="none" stroke="#8a8a94" stroke-width="1"/></svg></span>Velvet Harbor LLC</li>
        <li><span class="contact-icon"><svg width="10" height="8" viewBox="0 0 10 8"><rect x=".5" y=".5" width="9" height="7" fill="none" stroke="#8a8a94"/><path d="M.5 .5L5 4.5 9.5 .5" fill="none" stroke="#8a8a94"/></svg></span>hello@velvetharbor.com</li>
        <li><span class="contact-icon"><svg width="8" height="10" viewBox="0 0 8 10"><rect x="1" y=".5" width="6" height="9" rx="1" fill="none" stroke="#8a8a94"/><circle cx="4" cy="8" r=".6" fill="#8a8a94"/></svg></span>(212) 555-0148</li>
        <li><span class="contact-icon"><svg width="8" height="10" viewBox="0 0 8 10"><path d="M4 9.5C1.5 6 1 5 1 4a3 3 0 016 0c0 1-.5 2-3 5.5z" fill="none" stroke="#8a8a94"/><circle cx="4" cy="4" r="1" fill="#8a8a94"/></svg></span>Dana Morrow</li>
      </ul>
    </div>
    <div>
      <p class="col-title">Top rated Products</p>
      <ul class="mini">
        <li><span class="mini-name">Phones<span class="mini-price">$99 $119</span></span><span class="mini-thumb t-phones"></span></li>
        <li><span class="mini-name">Watches<span class="mini-price">$210</span></span><span class="mini-thumb t-watches"></span></li>
        <li><span class="mini-name">Sunglasses<span class="mini-price">$75 $60</span></span><span class="mini-thumb t-sunglasses"></span></li>
        <li><span class="mini-name">Fashion Hats<span class="mini-price">$38 $45</span></span><span class="mini-thumb t-hats"></span></li>
      </ul>
    </div>
    <div>
      <p class="col-title">Featured Products</p>
      <ul class="mini">
        <li><span class="mini-name">Sleek Sunglasses<span class="mini-price">$75</span></span><span class="mini-thumb t-sunglasses"></span></li>
        <li><span class="mini-name">Shoes Grey<span class="mini-price">$120</span></span><span class="mini-thumb t-shoes"></span></li>
        <li><span class="mini-name">Jacket Model<span class="mini-price">$175</span></span><span class="mini-thumb t-jacket"></span></li>
        <li><span class="mini-name">Headphones<span class="mini-price">$55 $68</span></span><span class="mini-thumb t-headphones"></span></li>
      </ul>
    </div>
    <div>
      <p class="col-title">On Sale</p>
      <ul class="mini">
        <li><span class="mini-name">Watches Class<span class="mini-price">$240 $210</span></span><span class="mini-thumb t-watches"></span></li>
        <li><span class="mini-name">Shoes Grey<span class="mini-price">$140 $120</span></span><span class="mini-thumb t-shoes"></span></li>
        <li><span class="mini-name">Bags-accessories<span class="mini-price">$99 $89</span></span><span class="mini-thumb t-bags"></span></li>
        <li><span class="mini-name">Fashion Hats<span class="mini-price">$45 $38</span></span><span class="mini-thumb t-hats"></span></li>
      </ul>
    </div>
  </div>
</footer>
<div class="footer-bottom"><strong>Velvet Harbor</strong><span>© Copyright 2012</span><span>—</span><span>All Rights Reserved</span></div>
</body>
</html>
```